Allied Health Clinic needs catchy poster ad for lightbox

We need a catchy and effective poster designed for our retail lightbox which is in a busy corridor. We are a multi disciplinary sports injury clinic offering a range of allied health services. Established in 1999. We need people to understand our business identity and services clearly. I have come up with a very rough idea as far as what I think the copy should contain. The picture is an example of what image I am trying to convey to the potential client. I am not a designer clearly. We specialise in treating difficult problems.
Size of the poster is 451mm x 741mm at 300dpi. We will then blow the image up to double this size which will be good enough resolution for the printing.

Target Market(s)

White collar professionals - male and female, active 20-50 range

Industry/Entity Type

Healthcare

Font styles to use
Sans Serif

Requirements
Nice to have
• Easy to read, polished, nice tie in to my logo colours

```html
<!DOCTYPE html>
<html lang="en">
<head>
<meta charset="utf-8">
<title>Stridewell Physiotherapy – Lightbox Poster</title>
<link rel="stylesheet" href="https://fonts.googleapis.com/css2?family=Open+Sans:ital,wght@0,400;0,600;0,700;1,700;1,800&display=swap">
<style>
  :root {
    --page-bg: #d6d6d6;
    --paper: #ecebe8;
    --paper-shade: #e1e0dc;
    --brand-green: #6cbd3e;
    --ink: #2a2a2a;
    --ink-soft: #3d3d3d;
    --photo-light: #d9d9d6;
    --photo-mid: #6d7585;
    --photo-dark: #1e2740;
  }
  * { box-sizing: border-box; margin: 0; padding: 0; }
  html, body { width: 1200px; height: 960px; overflow: hidden; }
  body {
    background: var(--page-bg);
    font-family: "Open Sans", Arial, sans-serif;
    color: var(--ink);
  }
  .poster {
    position: absolute;
    left: 280px; top: 28px;
    width: 640px; height: 904px;
    background: radial-gradient(ellipse at 40% 35%, var(--paper) 0%, var(--paper) 55%, var(--paper-shade) 100%);
    overflow: hidden;
  }
  .brand {
    position: absolute; right: 30px; top: 36px;
    display: flex; align-items: center; gap: 14px;
    color: var(--ink-soft); font-weight: 600;
  }
  .brand-dot { width: 42px; height: 42px; border-radius: 50%; background: var(--brand-green); }
  .brand-name { font-size: 17px; letter-spacing: 0.5px; line-height: 1.25; text-transform: uppercase; }
  .brand-name small { display: block; font-size: 11px; letter-spacing: 2.2px; }

  .headline-band {
    position: absolute; left: 0; top: 111px; width: 100%; height: 97px;
    background: var(--brand-green);
    text-align: center; color: var(--ink);
    padding-top: 10px;
  }
  .headline-band .line-1 { font-size: 33px; font-weight: 600; letter-spacing: 7px; line-height: 42px; }
  .headline-band .line-2 { font-size: 33px; font-weight: 700; letter-spacing: 1px; line-height: 42px; }

  .since {
    position: absolute; left: 28px; top: 232px;
    font-size: 28px; line-height: 36px; color: var(--ink-soft);
  }
  .since .lead { letter-spacing: 6px; }

  .services-tag { position: absolute; left: 0; top: 352px; width: 332px; height: 56px; }
  .services-tag span {
    position: absolute; left: 12px; top: 11px;
    font-size: 24px; color: var(--ink); white-space: nowrap;
  }

  .service-list { position: absolute; left: 28px; top: 450px; list-style: none; }
  .service-list li {
    font-size: 25px; font-weight: 800; font-style: italic;
    color: var(--brand-green); text-transform: uppercase;
    height: 60.5px; line-height: 32px;
  }

  .athlete-photo {
    position: absolute; left: 388px; top: 218px; width: 240px; height: 560px;
    border-radius: 120px 120px 40px 40px;
    background: linear-gradient(180deg, var(--photo-mid) 0%, var(--photo-dark) 45%, var(--photo-light) 62%, var(--photo-dark) 100%);
    opacity: 0.85;
  }

  .contact { position: absolute; left: 28px; display: flex; align-items: center; gap: 16px; color: var(--ink); }
  .contact svg { width: 40px; height: 40px; flex: none; }
  .contact.phone { top: 761px; font-size: 33px; }
  .contact.web { top: 817px; font-size: 17px; }

  .lifts {
    position: absolute; right: 38px; top: 786px; text-align: left;
    font-size: 25px; font-weight: 800; font-style: italic; line-height: 30px;
    text-transform: uppercase; color: var(--ink);
  }
  .lifts .take { letter-spacing: 7px; }
  .lifts .accent { color: var(--brand-green); }
</style>
</head>
<body>
  <main class="poster">
    <div class="brand">
      <span class="brand-dot"></span>
      <div class="brand-name">Stridewell Physiotherapy<small>&amp; Sports Injury Clinic</small></div>
    </div>

    <header class="headline-band">
      <div class="line-1">INJURY EXPERTS</div>
      <div class="line-2">TRUSTED BY ATHLETES</div>
    </header>

    <div class="athlete-photo" role="img" aria-label="Photo of a footballer in a navy kit striking a ball mid-air"></div>

    <p class="since"><span class="lead">SUCCESSFULLY</span><br>TREATING DIFFICULT<br>INJURIES SINCE 1999</p>

    <div class="services-tag">
      <svg width="332" height="56" viewBox="0 0 332 56" aria-hidden="true">
        <polygon points="0,0 314,0 332,28 314,56 0,56" fill="var(--brand-green)"/>
      </svg>
      <span>A Complete range of services:</span>
    </div>

    <ul class="service-list">
      <li>Sports Physiotherapy</li>
      <li>Chiropractic</li>
      <li>Massage</li>
      <li>Podiatry</li>
      <li>Exercise Physiology</li>
    </ul>

    <div class="contact phone">
      <svg viewBox="0 0 40 40" aria-hidden="true">
        <circle cx="20" cy="20" r="17" fill="none" stroke="var(--ink)" stroke-width="2.5"/>
        <path d="M11 17c0-3 4-5 9-5s9 2 9 5l-3 1-1-2c-3-1-7-1-10 0l-1 2z" fill="var(--ink)"/>
        <rect x="13" y="20" width="14" height="8" rx="2" fill="var(--ink)"/>
        <circle cx="20" cy="24" r="2" fill="var(--paper)"/>
      </svg>
      <span>8614 2270</span>
    </div>
    <div class="contact web">
      <svg viewBox="0 0 40 40" aria-hidden="true">
        <circle cx="20" cy="20" r="17" fill="none" stroke="var(--ink)" stroke-width="2.5"/>
        <circle cx="20" cy="20" r="10" fill="none" stroke="var(--ink)" stroke-width="1.8"/>
        <ellipse cx="20" cy="20" rx="4.5" ry="10" fill="none" stroke="var(--ink)" stroke-width="1.6"/>
        <line x1="10" y1="20" x2="30" y2="20" stroke="var(--ink)" stroke-width="1.6"/>
        <line x1="12" y1="15" x2="28" y2="15" stroke="var(--ink)" stroke-width="1.4"/>
        <line x1="12" y1="25" x2="28" y2="25" stroke="var(--ink)" stroke-width="1.4"/>
      </svg>
      <span>stridewellphysio.com.au</span>
    </div>

    <p class="lifts"><span class="take">TAKE</span><br><span class="accent">LIFTS TO</span><br>LEVEL 8</p>
  </main>
</body>
</html>
```